India March 15 Flyer

I would like a A4 Flyer made.
Very similair to attached file but the following changes
Name would be Explore Kerivan Weaving & Spice Journey

Cost $6995.00pp
16days fully escorted
Breakfast & Dinner included for 15days
Tour Departs Auckland 15th March 2015

Take out anything that is associated to Brisket Globe Voyages and it should be QMTrip Agents (attached) file for this.
Also no address just phone no's which is
09 573 8162
021736194
merel@qmtripagents.example.co.nz
QMTrip Agents Support Office:
Level 3, Pellor Finance Spire, 22-30 Quillane Rd,
Palmerston North 4493
Web:www.qmtripagents.example.co.nz
Under conditions take out Brisket Globe Voyages and put in QMTrip Agents and prices correct as at 20August 2014.
Under Conditions please change $400 deposit to $500 deposit pp.
Under Conditions: Price is Share Twin. Please advise if you want a single supplement cost.
I have attached a flyer that was done for me when i did the last tour. So this will give you an idea.
Also have attached the current itinerary that we will be doing for the March 2015 tour.
Hope this is enough information

Hello, Please do not forget to do the back of the flyer. dont put in itinerary but maybe a picture of the region that we are traveling and the Terms and Conditions which is so important. Thanks

I have noticed that the designs comming through dont have fully escorted by Merel Danforth which is a part of the brief with the flyer I included. Also return flights etc. Everything that was on the orginal flyer needs to include all of this except the Brisket Globe Voyages.

as this is a textile and culinary tour i would like to see pictures of textiles and food, as well as the normal pictures of India. I only seem to be getting elephant, taj extra but need to show the tour i am selling. Many thanks

Please re read the brief as i have made the required changes on this. IE: Price is now changed as well as some Terms and Conditions

• About Merel Danforth
• Pictures of Textiles and Culinerary as well as monuments

```html
<!DOCTYPE html>
<html lang="en">
<head>
<meta charset="utf-8">
<title>Explore Kerivan Weaving &amp; Spice Journey</title>
<link href="https://fonts.googleapis.com/css2?family=Archivo+Black&family=Montserrat:wght@400;700&family=Open+Sans:wght@600;700;800&display=swap" rel="stylesheet">
<style>
:root{
  --bg:#000;
  --paper:#fff;
  --green:#33f000;
  --green-text:#39d400;
  --ink:#111;
  --red:#e9161b;
  --blue:#1b2bc4;
  --orange:#ff4a16;
  --yellow:#f2b705;
}
*{box-sizing:border-box;margin:0;padding:0}
html,body{width:1200px;height:900px;overflow:hidden;background:var(--bg)}
body{position:relative;font-family:"Montserrat",Arial,sans-serif;color:var(--ink)}
.page{position:absolute;background:var(--paper);overflow:hidden}
.front{left:40px;top:58px;width:553px;height:782px}
.collage{position:absolute;left:0;top:0}
.title{position:absolute;font-family:"Archivo Black",Arial,sans-serif;white-space:nowrap}
.title-top{top:48px;left:52px;font-size:36px;letter-spacing:3px;color:#fff;-webkit-text-stroke:1.5px #444;text-shadow:2px 2px 3px rgba(0,0,0,.5)}
.title-mid{top:92px;left:118px;font-size:38px;
  background:linear-gradient(90deg,#e8161b,#f5a300,#ffe000,#2ecf00,#1aa0ff,#6a2bd8,#e8168a,#f5a300);
  -webkit-background-clip:text;background-clip:text;color:transparent;-webkit-text-stroke:1px #fff;filter:drop-shadow(2px 2px 2px rgba(0,0,0,.6))}
.title-end{top:148px;right:36px;font-size:34px;color:var(--green);-webkit-text-stroke:1.5px #000;text-shadow:2px 2px 2px rgba(0,0,0,.4)}
.intro{position:absolute;left:35px;top:370px;width:310px;font-size:16.5px;line-height:1.3;font-weight:400;color:#111}
.intro b{color:var(--green-text);font-weight:700}
.price-band{position:absolute;left:0;top:507px}
.price{position:absolute;left:48px;top:515px;font-family:"Open Sans",Arial,sans-serif;color:#111;font-weight:700}
.price .from{font-size:15px}
.price .amount{font-size:28px;color:#fff;font-weight:700}
.price .pp{font-size:14px}
.price .escort{font-size:16px;line-height:1.05;margin-top:-2px}
.price .include{font-size:15px;color:#fff;margin-top:8px}
.price .meals{font-size:13px;margin-top:3px}
.price .depart{font-size:11px;margin-top:3px}
.brand{position:absolute;display:flex;align-items:center;gap:6px}
.brand-mark{width:14px;height:14px;border-radius:50%;background:var(--green)}
.brand-name{font-family:"Montserrat",Arial,sans-serif;font-weight:700;font-size:19px;color:#111;letter-spacing:-.3px}
.brand-person{position:absolute;font-size:9px;font-weight:700;color:#111}
.front .brand{left:40px;top:662px}
.front .brand-person{left:100px;top:686px}
.contact{position:absolute;left:40px;top:702px;font-family:"Open Sans",Arial,sans-serif;font-size:9.3px;line-height:1.38;font-weight:600;color:#222}
.contact .label{color:var(--green-text)}
.back{left:617px;top:58px;width:505px;height:782px;background:var(--green)}
.back-sheet{position:absolute;left:10px;top:10px;width:386px;height:764px;background:var(--paper)}
.strip-edge{position:absolute;left:1122px;top:58px;width:48px;height:782px;background:var(--green)}
.photo-column{position:absolute;left:1018px;top:58px;width:104px;height:782px;background:#000}
.photo-column span{position:absolute;left:0;width:104px}
.back-sheet h2{position:absolute;left:21px;top:12px;font-family:"Archivo Black",Arial,sans-serif;font-weight:400;font-size:19px;color:#111}
.region{position:absolute;left:22px;top:50px;width:342px;height:470px;background:linear-gradient(160deg,#9fc2e6 0%,#d9c6a4 38%,#c7843f 62%,#8a4a2a 100%)}
.terms{position:absolute;left:22px;top:534px;width:342px}
.terms h3{font-family:"Archivo Black",Arial,sans-serif;font-weight:400;font-size:13px;color:var(--green-text);margin-bottom:4px}
.terms p{font-family:"Open Sans",Arial,sans-serif;font-size:7.4px;line-height:1.4;font-weight:600;color:#222}
.back .brand{left:110px;top:700px}
.back .brand-person{left:166px;top:724px}
</style>
</head>
<body>

<section class="page front">
  <svg class="collage" width="553" height="782" viewBox="0 0 553 782">
    <defs>
      <linearGradient id="ghats" x1="0" y1="0" x2="0" y2="1">
        <stop offset="0" stop-color="#8c8f95"/>
        <stop offset=".35" stop-color="#b7987a"/>
        <stop offset=".55" stop-color="#6b747a"/>
        <stop offset="1" stop-color="#41535d"/>
      </linearGradient>
      <linearGradient id="food" x1="0" y1="0" x2="1" y2="1"><stop offset="0" stop-color="#c9874a"/><stop offset="1" stop-color="#7a2e16"/></linearGradient>
      <linearGradient id="silk" x1="0" y1="0" x2="1" y2="0"><stop offset="0" stop-color="#e0207a"/><stop offset=".3" stop-color="#3b3fd0"/><stop offset=".6" stop-color="#e8a010"/><stop offset="1" stop-color="#c0182a"/></linearGradient>
      <linearGradient id="cloth" x1="0" y1="0" x2="1" y2="1"><stop offset="0" stop-color="#d2356a"/><stop offset="1" stop-color="#5a2a8a"/></linearGradient>
      <linearGradient id="snack" x1="0" y1="0" x2="1" y2="1"><stop offset="0" stop-color="#d9a55a"/><stop offset="1" stop-color="#8a5a2a"/></linearGradient>
      <linearGradient id="platter" x1="0" y1="0" x2="1" y2="1"><stop offset="0" stop-color="#e2e0d2"/><stop offset=".5" stop-color="#c2492a"/><stop offset="1" stop-color="#7a2412"/></linearGradient>
    </defs>
    <rect role="img" aria-label="Riverside ghats with boats on the river" x="0" y="0" width="553" height="300" fill="url(#ghats)"/>
    <path d="M0 275 Q300 120 553 275 L553 782 L0 782 Z" fill="#fff" stroke="#111" stroke-width="2"/>
    <polygon points="125,205 230,190 185,255" fill="var(--red)"/>
    <polygon points="292,190 420,182 355,248" fill="var(--blue)"/>
    <polygon role="img" aria-label="Plate of curry and flatbread" points="295,185 365,255 295,325 225,255" fill="url(#food)"/>
    <polygon role="img" aria-label="Colourful silk scarves hanging in rows" points="360,250 455,345 360,440 265,345" fill="url(#silk)"/>
    <polygon role="img" aria-label="Bright fabric scarves on display" points="460,195 535,270 460,345 385,270" fill="url(#silk)"/>
    <polygon points="520,310 610,400 520,490 430,400" fill="var(--orange)"/>
    <polygon role="img" aria-label="Folded patterned textiles" points="430,400 500,470 430,540 360,470" fill="url(#cloth)"/>
    <polygon role="img" aria-label="Fried puffed bread with curry" points="350,465 425,540 350,615 275,540" fill="url(#snack)"/>
    <polygon role="img" aria-label="Stacks of printed cloth" points="500,475 565,540 500,605 435,540" fill="url(#cloth)"/>
    <polygon points="553,520 470,605 553,690" fill="var(--yellow)"/>
    <polygon role="img" aria-label="Platter of grilled food with onion and lime" points="430,545 525,640 430,735 335,640" fill="url(#platter)"/>
    <polygon points="512,685 597,770 512,855 427,770" fill="var(--green)"/>
  </svg>

  <div class="title title-top">EXPLORE KERIVAN</div>
  <div class="title title-mid">Weaving &amp; Spice</div>
  <div class="title title-end">Journey</div>

  <p class="intro"><b>India</b> is one of the most captivating countries on earth - from its rich culture to breathtaking scenery. A trip to India will create memories to last you a lifetime.</p>

  <svg class="price-band" width="350" height="142" viewBox="0 0 350 142">
    <polygon points="0,0 300,0 345,71 300,142 0,142" fill="var(--green)"/>
  </svg>
  <div class="price">
    <div><span class="from">from </span><span class="amount">$6995.00</span><sup>*</sup><span class="pp">pp</span></div>
    <div class="escort">16days fully escorted by Merel Danforth</div>
    <div class="include">Include</div>
    <div class="meals">Breakfast &amp; Dinner for 15days</div>
    <div class="depart">Tour Departs Auckland 15th March 2015</div>
  </div>

  <div class="brand"><span class="brand-mark"></span><span class="brand-name">QMTrip Agents</span></div>
  <div class="brand-person">Merel Danforth</div>
  <div class="contact">
    <div><span class="label">T:</span> 09 573 8162, 021736194</div>
    <div><span class="label">E:</span> merel@qmtripagents.example.co.nz</div>
    <div>QMTrip Agents Support Office:</div>
    <div>Level 3, Pellor Finance Spire, 22-30 Quillane Rd, Palmerston North 4493</div>
    <div><span class="label">Web:</span> www.qmtripagents.example.co.nz</div>
  </div>
</section>

<section class="page back">
  <div class="back-sheet">
    <h2>The Region We Travel</h2>
    <div class="region" role="img" aria-label="Landscape of the northern region the tour travels through, with forts, desert and lakes"></div>
    <div class="terms">
      <h3>Terms &amp; Conditions</h3>
      <p>*Conditions Apply: Price is per person share twin from Auckland in Economy Class, including return flights, unless otherwise stated. Please advise if you want a single supplement cost. A $500 deposit per person is required to secure your place. A minimum of 14 people are required for this tour to be confirmed. All prices are in New Zealand dollars. Travel agent service fees are not included. Prices are correct as at 20 August 2014 &amp; may be subject to change without notice. Prices are based on payment by cash or EFTPOS only. Capacity may be limited &amp; may not be available on all flights. Offers valid for new bookings only. Accommodation is twin share. We welcome Corvane Pay Cardmembers. Product in this ad is supplied by suppliers with their own terms &amp; conditions, please ask your QMTrip Agents Professional for full terms &amp; conditions.</p>
    </div>
    <div class="brand"><span class="brand-mark"></span><span class="brand-name">QMTrip Agents</span></div>
    <div class="brand-person">Merel Danforth</div>
  </div>
</section>

<div class="photo-column">
  <span role="img" aria-label="Cycle rickshaw street scene" style="top:0;height:67px;background:linear-gradient(135deg,#9a7d6a,#c0392b)"></span>
  <span role="img" aria-label="Stone minaret seen through an arch" style="top:69px;height:78px;background:linear-gradient(180deg,#7fa6d6,#a0713f)"></span>
  <span role="img" aria-label="Domed monument with gardens" style="top:149px;height:53px;background:linear-gradient(180deg,#a9c8e8,#c9b79a)"></span>
  <span role="img" aria-label="River ghats with boats" style="top:204px;height:56px;background:linear-gradient(180deg,#b89a7c,#5a6f7c)"></span>
  <span role="img" aria-label="Train crossing open plains" style="top:262px;height:65px;background:linear-gradient(180deg,#b8c8d8,#a0804a)"></span>
  <span role="img" aria-label="White marble mausoleum with reflecting pool" style="top:329px;height:83px;background:linear-gradient(180deg,#9fc2e6,#e6e2d8 55%,#3f7a3a)"></span>
  <span role="img" aria-label="Market stall of colourful textiles" style="top:414px;height:78px;background:linear-gradient(135deg,#d2235a,#3040c0,#e09a10)"></span>
  <span role="img" aria-label="Decorated elephants at a fort gate" style="top:494px;height:73px;background:linear-gradient(180deg,#d8a070,#8a5a3a)"></span>
  <span role="img" aria-label="Block printing workshop" style="top:569px;height:73px;background:linear-gradient(135deg,#c8c2b8,#6a5a50)"></span>
  <span role="img" aria-label="Spice sacks at a market" style="top:644px;height:63px;background:linear-gradient(135deg,#e0a020,#c03a18,#6a3a1a)"></span>
  <span role="img" aria-label="Bazaar crowd with stalls" style="top:709px;height:73px;background:linear-gradient(180deg,#a09080,#5a4a3a)"></span>
</div>
<div class="strip-edge"></div>

</body>
</html>
```